Artisan Bread Company needs a business card

I need a business card design, for an artisan bread company called "Holloway's Bread".

I would like the logo on one side, and on the other, I would like it to say

Dorian Holloway
Baker
416.552.0193
hollowaysbread@breadmail.example

Not necessarily in that order- but it must have these.

Industry/Entity Type

Business

Font styles to use
Serif

Requirements
Must have
• The provided logo on the front, this on the back-
• Dorian Holloway
• Baker
• 416.552.0193
• hollowaysbread@breadmail.example

```html
<!DOCTYPE html>
<html lang="en">
<head>
<meta charset="utf-8">
<title>Holloway's Bread – Business Card</title>
<link href="https://fonts.googleapis.com/css2?family=Open+Sans:wght@300;400;600&family=Kalam:wght@400&display=swap" rel="stylesheet">
<style>
  :root {
    --page-bg: #e9e6e1;
    --card-dark: #0b0b0b;
    --card-light: #ffffff;
    --ink-dark: #1a1a1a;
    --ink-muted: #6b6b6b;
    --ink-light: #f4f4f4;
    --rule: #3a3a3a;
    --wheat-hi: #f2f2f2;
    --wheat-lo: #7a7a7a;
  }
  * { box-sizing: border-box; margin: 0; padding: 0; }
  html, body {
    width: 1200px; height: 843px; overflow: hidden;
    background: var(--page-bg);
    font-family: "Open Sans", Arial, sans-serif;
  }
  .canvas {
    position: relative; width: 1200px; height: 843px;
  }
  .card {
    position: absolute; top: 267px;
    width: 540px; height: 309px;
    border-radius: 22px;
    overflow: hidden;
    box-shadow: 0 10px 28px rgba(0,0,0,.18);
  }
  /* Logo side */
  .card--logo { left: 40px; background: var(--card-dark); color: var(--ink-light); }
  .wheat-art {
    position: absolute; left: 190px; top: 24px;
    width: 330px; height: 120px;
    border-radius: 60px 10px 60px 10px;
    background: linear-gradient(100deg, rgba(122,122,122,.0) 0%, var(--wheat-lo) 25%, var(--wheat-hi) 75%, #cfcfcf 100%);
    transform: rotate(-14deg);
    opacity: .9;
  }
  .logo-block { position: absolute; left: 38px; top: 168px; width: 260px; }
  .logo-name {
    font-weight: 300; font-size: 36px; letter-spacing: .5px; line-height: 1.1;
    color: var(--ink-light);
    display: flex; align-items: center; gap: 10px;
  }
  .logo-dot { width: 10px; height: 10px; border-radius: 50%; background: currentColor; flex: none; }
  .logo-rule { height: 1px; background: var(--ink-light); margin: 10px 0 8px; width: 240px; }
  .logo-web { font-size: 13px; letter-spacing: 2.5px; font-weight: 400; }

  /* Contact side */
  .card--contact { left: 620px; background: var(--card-light); color: var(--ink-dark); }
  .contact-logo {
    position: absolute; right: 34px; top: 44px; width: 230px; text-align: right;
  }
  .contact-logo .logo-name { color: var(--ink-dark); font-size: 30px; justify-content: flex-end; }
  .contact-logo .logo-rule { background: var(--ink-dark); width: 230px; margin: 8px 0 0 auto; }
  .person {
    position: absolute; left: 34px; top: 150px;
    font-family: "Kalam", cursive; font-size: 23px; letter-spacing: 1px;
    color: var(--ink-dark);
  }
  .contacts {
    position: absolute; left: 34px; right: 34px; top: 200px;
    display: flex; gap: 28px; font-size: 12.5px; color: var(--ink-muted);
  }
  .contact { display: flex; align-items: center; gap: 7px; }
  .contact svg { width: 12px; height: 12px; fill: var(--ink-dark); flex: none; }
  .contact-rule {
    position: absolute; left: 34px; right: 34px; top: 236px;
    height: 1px; background: var(--rule);
  }
  .contact--web { position: absolute; right: 34px; top: 252px; }
</style>
</head>
<body>
<main class="canvas">
  <section class="card card--logo">
    <div class="wheat-art" role="img" aria-label="Wheat stalk illustration in white and grey"></div>
    <div class="logo-block">
      <div class="logo-name"><span class="logo-dot"></span>Holloway's Bread</div>
      <div class="logo-rule"></div>
      <div class="logo-web">www.hollowaysbread.example</div>
    </div>
  </section>

  <section class="card card--contact">
    <div class="contact-logo">
      <div class="logo-name">Holloway's Bread</div>
      <div class="logo-rule"></div>
    </div>

    <p class="person">Dorian Holloway - Baker</p>

    <div class="contacts">
      <span class="contact">
        <svg viewBox="0 0 24 24" aria-hidden="true"><path d="M6.6 10.8a15.1 15.1 0 0 0 6.6 6.6l2.2-2.2a1 1 0 0 1 1-.25 11.4 11.4 0 0 0 3.6.57 1 1 0 0 1 1 1V20a1 1 0 0 1-1 1A17 17 0 0 1 3 4a1 1 0 0 1 1-1h3.5a1 1 0 0 1 1 1c0 1.25.2 2.45.57 3.6a1 1 0 0 1-.25 1z"/></svg>
        416.552.0193
      </span>
      <span class="contact">
        <svg viewBox="0 0 24 24" aria-hidden="true"><path d="M2 5h20v14H2z M4 7v.5l8 5 8-5V7l-8 5z" fill-rule="evenodd"/></svg>
        hollowaysbread@breadmail.example
      </span>
    </div>
    <div class="contact-rule"></div>
    <span class="contact contact--web" style="font-size:12.5px;color:var(--ink-muted);">
      <svg viewBox="0 0 24 24" aria-hidden="true"><circle cx="12" cy="12" r="10"/></svg>
      hollowaysbread.example
    </span>
  </section>
</main>
</body>
</html>
```